Business Cards Design for the electrical wholesaler: clean bold dynamic :)

We need a business card design that would follow our latest brand guidelines. As an electrical wholesaler we want to bring a fresh look and feel into the industry. The design should be clean bold and dynamic. It should come alive with the renewed energy of our green colour. Our grey colour should keep things balanced and complement the notion of maturity and responsibility. We employ Lato as a corporate font however are not bound by this font and we’re open to interpretation here.

Target Market(s)

Electrical contractors

Industry/Entity Type

Business

Contact Information for Business Card

Logo
Name & Surname: Olesia Hrybenko
Job Title: Director of Marketing
Email: olesia.hrybenko@mailvex.com
Cell phone: XXX.XXX.XXXX
Address: 20517 - 88 Ave. Edmonton, AB, Canada. T6K 2N8
Business Phone: 780.362.7048
Website: www.kopra.ca

Font styles to use
Other font styles liked:
• Lato

Requirements
Must have
• Logo & website
Nice to have
• Brand elements - some of them you may find in the attached Brand Guidelines (e.g. three lines on the background signifying "W")

```html
<!DOCTYPE html>
<html lang="en">
<head>
<meta charset="utf-8">
<title>Kopra Business Card</title>
<link href="https://fonts.googleapis.com/css2?family=Lato:wght@400;700;900&family=Saira:wght@600&display=swap" rel="stylesheet">
<style>
  :root {
    --backdrop: #3a3a3a;
    --card: #262627;
    --green: #7ed321;
    --grey: #c9c9c9;
    --white: #f2f2f2;
  }
  html, body {
    margin: 0;
    padding: 0;
    width: 799px;
    height: 1200px;
    overflow: hidden;
    background: var(--backdrop);
    font-family: "Lato", sans-serif;
  }
  .canvas {
    position: relative;
    width: 799px;
    height: 1200px;
  }
  .card {
    position: absolute;
    left: 90px;
    width: 620px;
    height: 354px;
    border-radius: 24px;
    background: var(--card);
    box-shadow: 0 14px 30px rgba(0,0,0,0.45);
    overflow: hidden;
  }
  .card--front { top: 113px; }
  .card--back { top: 733px; }

  .brand {
    position: absolute;
    display: flex;
    align-items: center;
    gap: 14px;
  }
  .brand__mark {
    background: var(--green);
    border-radius: 4px;
  }
  .brand__name {
    font-family: "Lato", sans-serif;
    font-weight: 900;
    color: var(--grey);
    line-height: 1;
    letter-spacing: 1px;
  }
  .card--front .brand {
    left: 50%;
    top: 50%;
    transform: translate(-50%, -50%);
  }
  .card--front .brand__mark { width: 56px; height: 56px; }
  .card--front .brand__name { font-size: 96px; }

  .card--back .brand {
    right: 42px;
    top: 60px;
    gap: 10px;
  }
  .card--back .brand__mark { width: 34px; height: 34px; }
  .card--back .brand__name { font-size: 56px; }

  .contact {
    position: absolute;
    left: 40px;
    bottom: 48px;
    color: var(--white);
  }
  .contact__name {
    font-family: "Saira", sans-serif;
    font-weight: 600;
    font-size: 26px;
    color: var(--green);
    margin: 0;
    line-height: 1.1;
  }
  .contact__title {
    font-size: 14px;
    margin: 4px 0 14px;
  }
  .contact__line {
    display: flex;
    align-items: center;
    gap: 8px;
    font-size: 14px;
    line-height: 22px;
  }
  .contact__line + .contact__line { margin-top: 2px; }
  .icon {
    width: 14px;
    height: 14px;
    flex: none;
  }
  .contact__gap { width: 10px; }
</style>
</head>
<body>
<main class="canvas">
  <section class="card card--front" aria-label="Card front">
    <div class="brand">
      <span class="brand__mark" aria-hidden="true"></span>
      <span class="brand__name">kopra</span>
    </div>
  </section>

  <section class="card card--back" aria-label="Card back">
    <div class="brand">
      <span class="brand__mark" aria-hidden="true"></span>
      <span class="brand__name">kopra</span>
    </div>

    <div class="contact">
      <h1 class="contact__name">Olesia Hrybenko</h1>
      <p class="contact__title">Founder &amp; CEO</p>
      <div class="contact__line">
        <svg class="icon" viewBox="0 0 14 14" aria-hidden="true"><circle cx="7" cy="7" r="7" fill="var(--green)"/><path d="M4.3 3.6l1.5-.3.8 1.9-.9.7a5 5 0 002.4 2.4l.7-.9 1.9.8-.3 1.5C7 10 4 7 4.3 3.6z" fill="var(--card)"/></svg>
        <span>+1 780-362-7048</span>
      </div>
      <div class="contact__line">
        <svg class="icon" viewBox="0 0 14 14" aria-hidden="true"><circle cx="7" cy="7" r="7" fill="var(--green)"/><rect x="3.5" y="4.5" width="7" height="5" fill="none" stroke="var(--card)" stroke-width="1"/><path d="M3.5 4.5L7 7.3l3.5-2.8" fill="none" stroke="var(--card)" stroke-width="1"/></svg>
        <span>olesia.hrybenko@mailvex.com</span>
        <span class="contact__gap"></span>
        <svg class="icon" viewBox="0 0 14 14" aria-hidden="true"><circle cx="7" cy="7" r="7" fill="var(--green)"/><circle cx="7" cy="7" r="3.6" fill="none" stroke="var(--card)" stroke-width="1"/><path d="M3.4 7h7.2M7 3.4c-1.6 2-1.6 5.2 0 7.2M7 3.4c1.6 2 1.6 5.2 0 7.2" fill="none" stroke="var(--card)" stroke-width="0.9"/></svg>
        <span>www.kopra.ca</span>
      </div>
      <div class="contact__line">
        <span>20517 - 88 Ave. Edmonton, AB, Canada T6K 2N8</span>
      </div>
    </div>
  </section>
</main>
</body>
</html>
```